Redesign Of Current Landing Page

I need to redesign this landing page https://www.brightoakpromos.biz/?page=landing&landing=23 (Please do not opt in because when you do it will show you the home page. Please clear your cookies before going to this url above to view the 1 page landing page.)

Please use my updated website as a reference for colors and logo.
http://layoutcraftzone.com/dh/bopg/index.html

I would like the call to action to be a button that opens into a lead form...

Button would be "Download Samples"

small business owners

Marketing

1 page

Designer to choose colors to be used in the design.

• must be full responsive on all devices
• must have a legitimate professional apeal to it
• open

```html
<!DOCTYPE html>
<html lang="en">
<head>
<meta charset="utf-8">
<title>Bright Oak Promos – Attract More Customers</title>
<link href="https://fonts.googleapis.com/css2?family=Montserrat:wght@400;600;700;800&family=Lato:wght@400;700&display=swap" rel="stylesheet">
<style>
:root{
  --blue:#0a6fc2;
  --blue-dark:#075fa8;
  --sky:#e6f1fa;
  --orange:#f26522;
  --ink:#333a40;
  --muted:#6d7479;
  --line:#d9dde1;
  --grey:#eef0f3;
  --white:#ffffff;
}
*{box-sizing:border-box;margin:0;padding:0}
html,body{width:718px;height:1200px;overflow:hidden}
body{position:relative;background:var(--white);font-family:"Lato",sans-serif;color:var(--ink)}
.abs{position:absolute}

/* header */
.site-header{left:0;top:0;width:718px;height:52px;background:var(--white)}
.brand{left:97px;top:15px;display:flex;align-items:center;gap:6px;font-family:"Montserrat",sans-serif;font-weight:700;font-size:12px;color:var(--blue);letter-spacing:.4px}
.brand-mark{width:14px;height:14px;background:var(--blue)}
.hours{left:497px;top:12px;text-align:center;font-family:"Montserrat",sans-serif;color:var(--blue)}
.hours b{display:block;font-size:21px;line-height:20px;font-weight:700}
.hours span{display:block;font-size:6px;letter-spacing:1.4px;color:var(--muted)}
.phones{left:541px;top:10px;font-family:"Montserrat",sans-serif;font-size:8.5px;color:var(--blue);line-height:17px}
.phones div{display:flex;align-items:center;gap:9px}
.phones svg{width:14px;height:11px}

/* hero */
.hero{left:0;top:52px;width:718px;height:278px;background:var(--sky)}
.hero-title{left:97px;top:92px;font-family:"Montserrat",sans-serif;font-weight:800;font-size:28px;line-height:36px;color:var(--blue);letter-spacing:.3px;white-space:nowrap}
.hero-sub{left:97px;top:170px;width:240px;font-family:"Montserrat",sans-serif;font-size:13px;line-height:16px;color:var(--blue)}
.btn{display:flex;align-items:center;justify-content:center;gap:8px;background:var(--blue);color:var(--white);font-family:"Montserrat",sans-serif;font-weight:600;font-size:11.5px}
.hero-btn{left:97px;top:227px;width:157px;height:36px}
.hero-visual{left:352px;top:50px;width:308px;height:296px;background:linear-gradient(135deg,#1f5fa8 0%,#3a8d3e 45%,#b0282a 80%,#4a2a1c 100%);box-shadow:0 6px 14px rgba(0,0,0,.25)}

/* about */
.about-band{left:0;top:330px;width:718px;height:470px;background:linear-gradient(#ffffff,#f7f8f9)}
.imagine{left:96px;top:421px;font-family:"Montserrat",sans-serif;font-weight:700;font-size:22px;color:var(--blue)}
.imagine span{color:#eceff2}
.copy{left:97px;width:250px;font-size:6.5px;line-height:10.8px;color:var(--ink)}
.copy p{margin-bottom:10px}
.copy strong{font-weight:400;font-size:7.2px}
.rule{left:123px;top:594px;width:170px;height:1px;background:var(--line)}
.how{left:96px;top:615px;font-family:"Montserrat",sans-serif;font-weight:700;font-size:21px;color:var(--orange)}
.why-title{left:410px;top:426px;width:226px;text-align:center;font-family:"Montserrat",sans-serif;font-weight:600;font-size:11.5px;color:#4a5157}
.why-rule{left:500px;top:451px;width:46px;height:1.5px;background:var(--blue)}
.why-axis{left:526px;top:500px;width:1.5px;height:225px;background:#a9cbe8}
.why-dot{width:6px;height:6px;border-radius:50%;background:var(--orange);left:523px}
.benefit{width:84px;text-align:center;font-size:6.2px;line-height:10px;color:var(--ink)}
.benefit svg{display:block;margin:0 auto 11px;width:26px;height:26px}
.section-split{left:8px;top:798px;width:702px;height:1px;background:#e6e9ec}

/* lead + testimonial */
.lead-band{left:0;top:799px;width:718px;height:356px;background:linear-gradient(#f6f7f8,var(--grey))}
.card{background:var(--white);border-radius:3px;box-shadow:0 1px 3px rgba(0,0,0,.05)}
.lead-card{left:97px;top:847px;width:260px;height:222px}
.lead-title{left:116px;top:870px;font-family:"Montserrat",sans-serif;font-weight:700;font-size:19px;color:var(--blue);white-space:nowrap}
.lead-title small{font-family:"Lato",sans-serif;font-weight:400;font-size:7px;color:var(--muted)}
.lead-note{left:116px;top:893px;font-size:7px;color:var(--muted);white-space:nowrap}
.field-label{font-size:7px;color:var(--ink)}
.field{height:24px;border:1px solid #c9d3dc;border-radius:2px;font-size:7px;color:#9aa1a7;padding:0 8px;display:flex;align-items:center}
.mandatory{left:289px;top:1016px;font-size:6px;color:var(--orange)}
.lead-btn{left:153px;top:1051px;width:148px;height:36px;font-size:11.5px}
.quote-card{left:410px;top:849px;width:213px;height:239px}
.quote-title{left:410px;top:865px;width:213px;text-align:center;font-family:"Montserrat",sans-serif;font-weight:600;font-size:11.5px;color:var(--blue)}
.quote-mark{left:423px;top:895px;font-family:"Montserrat",sans-serif;font-size:20px;color:#b5bbc0;line-height:1}
.quote-body{left:437px;top:899px;width:164px;font-size:6.8px;line-height:13.5px;color:var(--ink)}
.quote-name{left:470px;top:1051px;width:115px;text-align:right;font-size:8px;color:var(--blue)}
.quote-place{left:470px;top:1064px;width:134px;text-align:right;font-size:5.5px;color:var(--muted)}

/* footer */
.site-footer{left:0;top:1155px;width:718px;height:45px;background:var(--blue);color:var(--white);font-size:7px;display:flex;align-items:center;justify-content:center}
</style>
</head>
<body>

<header class="abs site-header"></header>
<div class="abs brand"><span class="brand-mark"></span>BRIGHT OAK PROMOS</div>
<div class="abs hours"><b>24</b><span>HOURS</span></div>
<div class="abs phones">
  <div><svg viewBox="0 0 14 11"><rect width="14" height="11" fill="#c9d7e6"/><rect y="0" width="14" height="2" fill="#d33"/><rect y="4.5" width="14" height="2" fill="#d33"/><rect y="9" width="14" height="2" fill="#d33"/></svg>555-410-2286</div>
  <div><svg viewBox="0 0 14 11"><circle cx="7" cy="5.5" r="5.5" fill="#2a8ad6"/></svg>1-800-555-0147</div>
</div>

<section class="abs hero"></section>
<div class="abs hero-visual" role="img" aria-label="Fanned stack of printed incentive certificates: cash back reward, hotel stay, cruise, MP4 player and Las Vegas trip"></div>
<h1 class="abs hero-title">ATTRACT MORE<br>CUSTOMERS</h1>
<p class="abs hero-sub">who spend more money with your busines moreo ften!</p>
<div class="abs btn hero-btn">Download Samples
  <svg width="16" height="6" viewBox="0 0 16 6"><path d="M0 3h14M11 .5 15 3l-4 2.5" stroke="#fff" fill="none" stroke-width="1"/></svg>
</div>

<section class="abs about-band"></section>
<h2 class="abs imagine">Imagine <span>we promote</span></h2>
<div class="abs copy" style="top:465px">
  <p>being able to create exciting give away promotions that will boost your sales without ever having to worry about cost.</p>
  <p><strong>Bright Oak Promo Group, Inc.</strong> provides high-perceived value promotional incentives to businesses that want to advertise an exciting Give Away that will instantly attract more customers from your existing advertising efforts.</p>
  <p>Your business can give away incentive certificates that are redeemable for luxury hotel &amp; resort stays with airfare included, <strong>cruises, cash for gas, groceries, dining and even electronic goods.</strong></p>
</div>
<div class="abs rule"></div>
<h2 class="abs how">How can we do it?</h2>
<div class="abs copy" style="top:659px">
  <p>We help fill empty rooms for thousands of hotels and resorts in hundreds of destinations around the world as well as the major cruise lines. Hotels and resorts are rarely full so when we place someone in their empty rooms, they end up making it up when travelers spend money on room service, spa services, eat at their in-house restaurants, casino and take advantage of other amenities that drive revenue.</p>
  <p><strong>We also help over 18,000 restaurants, electronic manufacturers, the major gas companies and top grocery chains in the U.S and Canada increase brand awareness as well as increase customer loyalty.</strong></p>
</div>

<h3 class="abs why-title">Why Offer Incentives To Customers?</h3>
<div class="abs why-rule"></div>
<div class="abs why-axis"></div>
<div class="abs why-dot" style="top:512px"></div>
<div class="abs why-dot" style="top:611px"></div>
<div class="abs why-dot" style="top:706px"></div>

<div class="abs benefit" style="left:426px;top:474px">
  <svg viewBox="0 0 26 26"><rect x="3" y="14" width="5" height="11" fill="#2a8ad6"/><rect x="10" y="10" width="5" height="15" fill="#2a8ad6"/><rect x="17" y="6" width="5" height="19" fill="#2a8ad6"/><path d="M3 11 11 4" stroke="#5cb531" stroke-width="3" fill="none"/><path d="M8 3h5v5z" fill="#5cb531"/></svg>
  Increase Responses From Your Existing Ads</div>
<div class="abs benefit" style="left:541px;top:474px">
  <svg viewBox="0 0 26 26"><circle cx="9" cy="8" r="5.5" fill="#9aa3ab"/><path d="M12 11 22 21" stroke="#c0392b" stroke-width="4" stroke-linecap="round"/></svg>
  #1 Sales Closing Tool - Gift w/ Purchase</div>
<div class="abs benefit" style="left:426px;top:572px">
  <svg viewBox="0 0 26 26"><path d="M13 1l3.6 7.6 8.3 1-6.1 5.7 1.6 8.2L13 19.4 5.6 23.5l1.6-8.2L1.1 9.6l8.3-1z" fill="#f5a516"/></svg>
  Build Brand Awareness and Trust</div>
<div class="abs benefit" style="left:541px;top:572px">
  <svg viewBox="0 0 26 26"><circle cx="9" cy="7" r="4" fill="#5cb531"/><rect x="3" y="12" width="12" height="11" rx="4" fill="#5cb531"/><circle cx="17" cy="10" r="4" fill="#2a8ad6"/><rect x="11" y="15" width="12" height="10" rx="4" fill="#2a8ad6"/></svg>
  Insure The Sale Over Your Competition</div>
<div class="abs benefit" style="left:426px;top:669px">
  <svg viewBox="0 0 26 26"><path d="M4 9h14M14 4l6 5-6 5" stroke="#2a8ad6" stroke-width="3" fill="none"/><path d="M22 18H8M12 13l-6 5 6 5" stroke="#8aa0b3" stroke-width="3" fill="none"/></svg>
  Boost Repeat and Referral Business-</div>
<div class="abs benefit" style="left:541px;top:669px">
  <svg viewBox="0 0 26 26"><circle cx="13" cy="13" r="11" fill="#2a8ad6"/><text x="13" y="18" text-anchor="middle" font-family="Montserrat,sans-serif" font-weight="700" font-size="14" fill="#fff">$</text></svg>
  Improve Retention Rates</div>

<div class="abs section-split"></div>

<section class="abs lead-band"></section>
<div class="abs card lead-card"></div>
<h2 class="abs lead-title">Enter your info <small>to be forward to our</small></h2>
<p class="abs lead-note">website for the all details and to recive sample in your email!</p>
<label class="abs field-label" style="left:115px;top:931px">Full name*</label>
<label class="abs field-label" style="left:231px;top:931px">Phone*</label>
<div class="abs field" style="left:115px;top:944px;width:108px">john doe</div>
<div class="abs field" style="left:229px;top:944px;width:108px">+88-1234567</div>
<label class="abs field-label" style="left:117px;top:978px">Email*</label>
<div class="abs field" style="left:115px;top:990px;width:222px">johndoe@mailbox.com</div>
<span class="abs mandatory">*mandatory field</span>
<div class="abs btn lead-btn">Download Samples</div>

<div class="abs card quote-card"></div>
<h3 class="abs quote-title">Client testimonials</h3>
<span class="abs quote-mark">“</span>
<p class="abs quote-body">I began using your incentives two years ago to boost lead generation efforts. I have experienced a 63% increase in lead captures. And, even more importantly, my sales have increased as well. The ability to offer unlimited certificates and not having to pay for each certificate I give away is perhaps the best feature of the program, but having the flexibility to email or print certificates for my customers is also wonderful. I even use your html banners to automate my promotions right on my website!,</p>
<p class="abs quote-name">Dale R.</p>
<p class="abs quote-place">Riverton, TN</p>

<footer class="abs site-footer">© 2005-2017 Bright Oak Promo Group, Inc. - All Rights Reserved</footer>

</body>
</html>
```